Rig up a website for a Rigging Company

We already have a logo. Looking for a website design that works on plinvara.com.
Our rigging company uses semi trucks, forklifts, and similar equipment to move large machines.
Our logo is white, black and red.

Target Market(s)

Medical Industry (moving medical equipment), Utility Industry (power equipment), Food Industry (moving bottling/packing equipment), US Government (large equipment)

Industry/Entity Type

It Company

Coding

Coded - Design and coding required

Number of Pages Required

5+ page

Font styles to use
Sans Serif

Colors
ec1f27
ffffff
0355a3

Requirements
Must have
• Home page, About page, Services Page, and Contact Information page
Nice to have
• Pictures of semi and forklifts and ability to insert our own pictures of our equipment

```html
<!DOCTYPE html>
<html lang="en">
<head>
<meta charset="utf-8">
<title>Halvor Rigging</title>
<link href="https://fonts.googleapis.com/css2?family=Roboto:ital,wght@0,300;0,400;0,500;0,700;1,300;1,400&display=swap" rel="stylesheet">
<style>
:root{
  --red:#e8333a;
  --red-soft:#f07075;
  --ink:#1d1d1d;
  --text:#444;
  --muted:#8a8a8a;
  --band:#f1f1f1;
  --bar:#ececec;
  --white:#fff;
  --field:#efefef;
  --map:#dfe3e6;
}
*{margin:0;padding:0;box-sizing:border-box}
html,body{width:1200px;height:2169px;overflow:hidden}
body{font-family:'Roboto',sans-serif;color:var(--text);background:var(--white);position:relative}
.abs{position:absolute}
section,header,footer{position:absolute;left:0;width:1200px}
.top-line{top:0;height:4px;background:var(--red)}
.site-header{top:4px;height:71px;background:var(--white)}
.brand{left:52px;top:17px;font-weight:700;font-size:27px;color:var(--ink);letter-spacing:.5px;display:flex;align-items:center;gap:8px}
.brand .dot{width:14px;height:14px;background:var(--red);border-radius:50%}
.main-nav{left:458px;top:24px;display:flex;gap:38px;font-size:14px;color:var(--ink)}
.chat{left:969px;top:24px;font-size:13px;color:var(--ink);display:flex;gap:5px;align-items:center}
.quote-btn{left:1032px;top:16px;width:122px;height:32px;background:var(--red);color:var(--white);border-radius:6px;font-size:14px;font-weight:500;display:flex;align-items:center;justify-content:center}
.hero{top:75px;height:490px;background:linear-gradient(180deg,#7f8791 0%,#a9adb2 35%,#c7c2bb 55%,#8b8f94 72%,#6c7075 100%)}
.hero-badge{left:499px;top:135px;width:202px;height:202px;border-radius:50%;background:rgba(120,116,112,.72);color:var(--white);text-align:center;display:flex;flex-direction:column;justify-content:center;font-size:24px;font-weight:300;letter-spacing:1.5px;line-height:1.2}
.hero-badge b{font-size:31px;font-weight:700}
.info-bar{top:565px;height:34px;background:var(--bar);font-size:13px;color:var(--muted)}
.info-bar .item{top:9px;display:flex;gap:6px;align-items:center}
.social-sq{top:9px;width:16px;height:16px;border-radius:2px}
.sec-title{left:0;width:1200px;text-align:center;font-size:21px;font-weight:700;color:var(--ink)}
.sec-title span{color:var(--red)}
.dash{left:52px;width:1096px;border-top:1px dashed var(--red)}
.welcome{top:599px;height:114px;background:var(--white)}
.welcome p{left:52px;width:1096px;top:64px;font-size:13px;text-align:center;line-height:20px;color:#333}
.services{top:713px;height:309px;background:var(--band)}
.card{top:114px;width:253px;height:168px}
.card .photo{height:126px}
.card .label{height:42px;background:linear-gradient(90deg,var(--red),var(--red-soft));color:var(--white);font-size:14px;display:flex;align-items:center;justify-content:center;border-radius:0 0 22px 0}
.process{top:1022px;height:274px;background:var(--white)}
.step{top:105px;width:96px;height:96px;margin-left:-48px;border-radius:50%;background:var(--red);box-shadow:0 0 0 3px #f5c9cb;display:flex;align-items:center;justify-content:center}
.step.active{box-shadow:0 0 0 3px var(--white),0 0 0 5px var(--red)}
.step-label{top:226px;width:160px;margin-left:-80px;text-align:center;font-size:13px;font-weight:700;color:var(--ink)}
.step-label.active{color:var(--red)}
.link{top:153px;height:1px;background:#d9a5a7}
.reviews{top:1296px;height:357px;background:var(--band)}
.quote{font-size:13px;font-style:italic;font-weight:300;line-height:20px;color:#555;width:410px}
.quote.right-al{text-align:right}
.who{font-size:13px;font-weight:400;color:var(--ink);font-style:normal;margin-top:9px}
.avatar{width:78px;height:78px;border-radius:50%;background:radial-gradient(circle at 50% 40%,#d7c3b3,#8e8079)}
.mail{top:1653px;height:94px;background:var(--white)}
.mail .field{top:30px;width:253px;height:32px;background:var(--field);border:1px solid #e2e2e2;border-radius:3px;font-size:13px;color:#b5b5b5;padding:8px 14px}
.submit{left:1057px;top:30px;width:90px;height:32px;background:var(--red);color:var(--white);font-size:13px;font-weight:500;border-radius:3px;display:flex;align-items:center;justify-content:center}
.site-footer{top:1747px;height:422px;background:var(--band)}
.site-footer h3{font-size:18px;font-weight:500;color:var(--ink)}
.col-text{font-size:13px;line-height:20px;color:#333}
.col-text b{font-weight:500;color:var(--ink)}
.map{left:334px;top:66px;width:535px;height:226px;background:var(--map)}
.foot-line{left:52px;top:345px;width:1096px;border-top:1px solid #555}
.bottom-line{top:2165px;height:4px;background:var(--red)}
</style>
</head>
<body>
<div class="abs top-line" style="left:0;width:1200px"></div>

<header class="site-header">
  <div class="abs brand"><span class="dot"></span>Halvor Rigging</div>
  <nav class="abs main-nav"><span>Our Company</span><span>Services</span><span>Contact Us</span></nav>
  <div class="abs chat">Chat
    <svg width="14" height="12" viewBox="0 0 14 12"><path d="M1 1h10v6H5l-3 3V7H1z" fill="none" stroke="#1d1d1d" stroke-width="1.3"/></svg>
  </div>
  <div class="abs quote-btn">Request a Quote</div>
</header>

<section class="hero" role="img" aria-label="Forklift carrying a wooden crate beside a warehouse at a harbour under a cloudy sky">
  <div class="abs hero-badge"><span>ARE YOU</span><b>LOOKING</b><span>FOR</span><span>FORKLIFTS</span></div>
</section>

<section class="info-bar">
  <div class="abs item" style="left:52px">
    <svg width="11" height="11" viewBox="0 0 12 12"><path d="M2 1l2 0 1 3-1.5 1a7 7 0 0 0 3.5 3.5L8 7l3 1v2a1 1 0 0 1-1 1A9 9 0 0 1 1 2a1 1 0 0 1 1-1z" fill="#8a8a8a"/></svg>+1 800 555 01 72</div>
  <div class="abs item" style="left:200px">
    <svg width="13" height="10" viewBox="0 0 13 10"><rect width="13" height="10" fill="#8a8a8a"/><path d="M0 0l6.5 5L13 0" fill="none" stroke="#ececec"/></svg>info@plinvara.com</div>
  <div class="abs social-sq" style="left:1000px;background:#3b5998"></div>
  <div class="abs social-sq" style="left:1043px;background:#2ea7df"></div>
  <div class="abs social-sq" style="left:1085px;background:#dd4b39"></div>
  <svg class="abs" style="left:1134px;top:10px" width="14" height="14" viewBox="0 0 14 14"><circle cx="6" cy="6" r="4.5" fill="none" stroke="#8a8a8a" stroke-width="1.6"/><path d="M9.5 9.5L13 13" stroke="#8a8a8a" stroke-width="1.8"/></svg>
</section>

<section class="welcome">
  <h2 class="abs sec-title" style="top:18px">Welcome to <span>Halvor Rigging</span></h2>
  <div class="abs dash" style="top:46px"></div>
  <p class="abs">Sed ut perspiciatis unde omnis iste natus error sit voluptatem accusantium doloremque laudantium, totam rem aperiam, eaque ipsa quae ab illo inventore veritatis et quasi architecto beatae vitae dicta sunt explicabo.</p>
</section>

<section class="services">
  <h2 class="abs sec-title" style="top:17px">Our <span>Services</span></h2>
  <div class="abs dash" style="top:56px"></div>
  <div class="abs card" style="left:52px"><div class="photo" role="img" aria-label="Semi truck hauling a trailer on a highway" style="background:linear-gradient(160deg,#d9a35b,#6f7fa6 60%,#3b4768)"></div><div class="label">Ground Shipping</div></div>
  <div class="abs card" style="left:333px"><div class="photo" role="img" aria-label="Forklift moving a wrapped pallet in a warehouse" style="background:linear-gradient(160deg,#3a2f2a,#8a7260 55%,#c9b59a)"></div><div class="label">Forwarding Services</div></div>
  <div class="abs card" style="left:614px"><div class="photo" role="img" aria-label="Warehouse aisle with shelves of packaged goods" style="background:linear-gradient(180deg,#7b6b56,#c8b08a 55%,#9a8a72)"></div><div class="label">Packaged Goods</div></div>
  <div class="abs card" style="left:895px"><div class="photo" role="img" aria-label="Worker on a pallet truck in a warehouse" style="background:linear-gradient(160deg,#6d6a66,#b9a487 55%,#d4c9b6)"></div><div class="label">Warehousing</div></div>
</section>

<section class="process">
  <h2 class="abs sec-title" style="top:10px">Process <span>Cargo</span></h2>
  <div class="abs dash" style="top:49px"></div>
  <div class="abs link" style="left:193px;width:65px"></div>
  <div class="abs link" style="left:380px;width:65px"></div>
  <div class="abs link" style="left:567px;width:65px"></div>
  <div class="abs link" style="left:752px;width:65px"></div>
  <div class="abs link" style="left:938px;width:65px"></div>

  <div class="abs step" style="left:132px"><svg width="50" height="50" viewBox="0 0 50 50" fill="none" stroke="#fff" stroke-width="2"><path d="M10 16l16-7 15 7v18l-15 7-16-7z M10 16l16 7 15-7 M26 23v18"/><circle cx="14" cy="36" r="6" fill="#e8333a"/><path d="M11 36l2 2 4-4"/></svg></div>
  <div class="abs step" style="left:318px"><svg width="50" height="50" viewBox="0 0 50 50" fill="none" stroke="#fff" stroke-width="2"><rect x="14" y="12" width="22" height="28"/><rect x="17" y="8" width="16" height="5"/><path d="M18 20h14M18 25h14M18 30h14M18 35h10"/></svg></div>
  <div class="abs step" style="left:506px"><svg width="50" height="50" viewBox="0 0 50 50" fill="none" stroke="#fff" stroke-width="2"><rect x="10" y="12" width="18" height="16"/><path d="M15 22v-6l-2 2M15 16l2 2M22 22v-6l-2 2M22 16l2 2M31 20h9M36 16l4 4-4 4"/><rect x="8" y="31" width="34" height="8" rx="4"/><circle cx="14" cy="35" r="1.5"/><circle cx="21" cy="35" r="1.5"/><circle cx="28" cy="35" r="1.5"/><circle cx="35" cy="35" r="1.5"/></svg></div>
  <div class="abs step" style="left:693px"><svg width="50" height="50" viewBox="0 0 50 50" fill="none" stroke="#fff" stroke-width="2"><path d="M6 14h24v19H6z M30 20h7l6 7v6H30"/><circle cx="13" cy="36" r="3"/><circle cx="36" cy="36" r="3"/><path d="M11 23h12M19 19l4 4-4 4"/></svg></div>
  <div class="abs step active" style="left:876px"><svg width="50" height="50" viewBox="0 0 50 50" fill="none" stroke="#fff" stroke-width="2"><rect x="14" y="8" width="22" height="34"/><rect x="19" y="16" width="5" height="5"/><rect x="26" y="16" width="5" height="5"/><rect x="19" y="26" width="5" height="5"/><rect x="26" y="26" width="5" height="5"/></svg></div>
  <div class="abs step" style="left:1060px"><svg width="50" height="50" viewBox="0 0 50 50" fill="none" stroke="#fff" stroke-width="2"><rect x="8" y="13" width="22" height="18"/><path d="M30 18h7l5 6v7H30"/><circle cx="15" cy="35" r="3"/><circle cx="35" cy="35" r="3"/></svg></div>

  <div class="abs step-label" style="left:132px">Receive / Sender</div>
  <div class="abs step-label" style="left:318px">Transera</div>
  <div class="abs step-label" style="left:506px">Supplier</div>
  <div class="abs step-label" style="left:693px">Carrier</div>
  <div class="abs step-label active" style="left:876px">Transera</div>
  <div class="abs step-label" style="left:1060px">Shipped</div>
</section>

<section class="reviews">
  <h2 class="abs sec-title" style="top:17px">What <span>People Say</span></h2>
  <div class="abs dash" style="top:54px"></div>
  <div class="abs" style="left:600px;top:101px;height:218px;border-left:1px dashed var(--red)"></div>
  <div class="abs dash" style="top:211px"></div>

  <div class="abs quote right-al" style="left:52px;top:101px">Duis aute irure dolor in reprehenderit in voluptate velit esse cillum dolore eu fugiat nulla pariatur. Excepteur sint occaecat cupidatat non proident, sunt in culpa qui officia deserunt mollit.<div class="who">Evan Marsh, Operations Manager</div></div>
  <div class="abs avatar" role="img" aria-label="Portrait of a reviewer" style="left:490px;top:99px"></div>
  <div class="abs avatar" role="img" aria-label="Portrait of a reviewer" style="left:633px;top:99px"></div>
  <div class="abs quote" style="left:739px;top:101px">Provident, similique sunt in culpa qui officia deserunt mollitia animi, id est laborum et dolorum fuga. Et harum quidem rerum facilis est et expedita distinctio. Nam libero tempore, cum soluta nobis.<div class="who">Nora Fields, Creative Designer</div></div>

  <div class="abs quote right-al" style="left:52px;top:239px">Luis aute irure dolor in reprehenderit in piluptate velit esse cillum dolore eu fugiat nulla pariatur. Excepteur sint occaecat cupidatat non proident, sunt in culpa qui officia deserunt mollit.<div class="who">Clara Voss, Manager</div></div>
  <div class="abs avatar" role="img" aria-label="Portrait of a reviewer" style="left:490px;top:238px"></div>
  <div class="abs avatar" role="img" aria-label="Portrait of a reviewer" style="left:633px;top:238px"></div>
  <div class="abs quote" style="left:739px;top:239px">At vero eos et accusamus et iusto odio dignissimos ducimus qui blanditiis praesentium voluptatum deleniti atque corrupti quos dolores et quas molestias excepturi sint occaecati asperiores.<div class="who">Owen Pike, Developer</div></div>
</section>

<section class="mail">
  <svg class="abs" style="left:52px;top:28px" width="34" height="32" viewBox="0 0 34 32" fill="none" stroke="#e8333a" stroke-width="2" stroke-linejoin="round"><path d="M2 14L32 2 24 30 16 20z M16 20L32 2 M16 20l-2 9 5-6"/></svg>
  <div class="abs" style="left:113px;top:38px;font-size:13px;font-weight:500;color:var(--ink)">Feel Free to Mail</div>
  <div class="abs field" style="left:240px">Full Name *</div>
  <div class="abs field" style="left:512px">Phone Number *</div>
  <div class="abs field" style="left:784px">Your Email *</div>
  <div class="abs submit">SUBMIT</div>
</section>

<footer class="site-footer">
  <h3 class="abs" style="left:52px;top:24px">Contact Us</h3>
  <div class="abs col-text" style="left:52px;top:65px;width:250px">
    <p>Please feel free to contact us for any issue. Our staff is available to you from 9AM until 5PM on weekdays.</p>
    <p style="margin-top:14px"><b>Phone:</b> +1 800-555-0148</p>
    <p style="margin-top:14px"><b>Office:</b> Harborview Depot</p>
    <p style="margin-top:14px"><b>Email:</b> info@plinvara.com</p>
  </div>
  <div class="abs" style="left:52px;top:248px;display:flex;gap:14px">
    <span style="width:12px;height:12px;border-radius:50%;background:#1d1d1d"></span>
    <span style="width:12px;height:12px;border-radius:50%;background:#1d1d1d"></span>
    <span style="width:12px;height:12px;border-radius:50%;background:#1d1d1d"></span>
    <span style="width:12px;height:12px;border-radius:50%;background:#1d1d1d"></span>
    <span style="width:12px;height:12px;border-radius:50%;background:#1d1d1d"></span>
  </div>

  <h3 class="abs" style="left:334px;width:535px;text-align:center;top:24px">Headquarters</h3>
  <div class="abs map" role="img" aria-label="Map showing the headquarters location"></div>

  <h3 class="abs" style="left:896px;top:24px">About Team</h3>
  <div class="abs col-text" style="left:896px;top:65px;width:252px">
    <p>Enim congue blandit. Lorem ipsum dolor sit amet, consectetur adipiscing elit. Quisque consectetur interdum finibus. Vestibulum ante ipsum primis in faucibus orci. luctus et ultrices posuere.</p>
    <p style="margin-top:14px">Cubilia cras blandit finibus ipsum, id porttitor arcu volutpat a. Integer iaculis erat nec justo malesuada faucibus vel tempus sapien. Vivamus aliquam euismod tristique.</p>
  </div>

  <div class="abs foot-line"></div>
  <div class="abs" style="left:52px;top:372px;font-size:12px;color:var(--ink)">Copyright © 2017 Halvor Rigging</div>
  <div class="abs" style="left:0;width:1200px;top:364px;text-align:center;font-size:22px;font-weight:700;color:var(--ink)">Halvor Rigging</div>
  <div class="abs" style="left:1000px;width:148px;text-align:right;top:372px;font-size:12px;color:var(--ink)">All rights reserved</div>
</footer>
<div class="abs bottom-line" style="left:0;width:1200px"></div>
</body>
</html>
```